Bref créative
Limb Nestler
Naturally made in the US
Professional
Rosalind Featherstone
Owner
437 Tamsin Ave - Ste 220-581
rfeatherstone@limbnestler-example.com
Limbnestler-example.com
I'm not sure what the first two boxes refer to. I want our logo to be on the cards in the same colors.

```html
<!DOCTYPE html>
<html lang="en">
<head>
<meta charset="utf-8">
<title>Limb Nestler – Business Card</title>
<link rel="stylesheet" href="https://fonts.googleapis.com/css2?family=Open+Sans:wght@400;600;700&display=swap">
<style>
  :root {
    --page-bg: #ece9e4;
    --card-white: #ffffff;
    --brand-blue: #1d95d3;
    --brand-maroon: #6e1f24;
    --text-dark: #3a2a2a;
    --text-grey: #5a5a5a;
    --text-light: #ffffff;
  }
  * { margin: 0; padding: 0; box-sizing: border-box; }
  html, body {
    width: 1200px; height: 965px; overflow: hidden;
    background: var(--page-bg);
    font-family: "Open Sans", Arial, sans-serif;
  }
  .business-card {
    position: absolute;
    left: 120px; top: 208px;
    width: 960px; height: 548px;
    border-radius: 26px;
    overflow: hidden;
    background: var(--card-white);
    box-shadow: 0 6px 18px rgba(0,0,0,.18);
  }
  .card-shape { position: absolute; inset: 0; }
  .holder-name {
    position: absolute; left: 42px; top: 34px;
    color: var(--text-light);
    font-size: 33px; font-weight: 700;
  }
  .holder-role {
    position: absolute; left: 42px; top: 78px;
    color: var(--brand-maroon);
    font-size: 23px; font-weight: 600;
  }
  .contact-list {
    position: absolute; left: 42px; top: 322px;
    list-style: none;
    color: var(--text-dark);
    font-size: 18.5px;
  }
  .contact-list li { display: flex; align-items: center; height: 35px; white-space: nowrap; }
  .contact-list .address { margin-bottom: 4px; }
  .contact-list svg { width: 20px; height: 20px; margin-right: 12px; flex: none; }
  .brand-block {
    position: absolute; left: 580px; top: 220px; width: 340px;
    text-align: center;
  }
  .brand-name {
    display: flex; align-items: center; justify-content: center; gap: 14px;
    color: var(--brand-maroon);
    font-size: 50px; font-weight: 400; line-height: 1;
  }
  .brand-dot {
    width: 30px; height: 30px; border-radius: 50%;
    background: var(--brand-blue);
  }
  .brand-tagline {
    margin-top: 10px;
    color: var(--text-grey);
    font-size: 17px;
    padding-left: 44px;
  }
</style>
</head>
<body>
  <div class="business-card">
    <svg class="card-shape" viewBox="0 0 960 548" width="960" height="548" aria-hidden="true">
      <path fill="var(--brand-maroon)"
        d="M0 0 H450 C 560 40, 556 160, 502 255 C 472 325, 482 450, 545 548 H0 Z"/>
      <path fill="var(--card-white)"
        d="M0 0 H437 C 532 40, 530 152, 478 252 C 458 320, 478 442, 545 548 H0 Z"/>
      <path fill="var(--brand-blue)"
        d="M0 0 H430 C 520 40, 520 150, 470 250 C 450 320, 470 440, 540 548 H0 Z"/>
    </svg>

    <div class="holder-name">Rosalind Featherstone</div>
    <div class="holder-role">Owner</div>

    <ul class="contact-list">
      <li class="address">437 Tamsin Ave - Ste 220-581</li>
      <li>
        <svg viewBox="0 0 24 24"><path fill="#fff" d="M6.6 10.8a15 15 0 0 0 6.6 6.6l2.2-2.2c.3-.3.7-.4 1-.2 1.1.4 2.3.6 3.6.6.6 0 1 .4 1 1V20c0 .6-.4 1-1 1C10.6 21 3 13.4 3 4c0-.6.4-1 1-1h3.5c.6 0 1 .4 1 1 0 1.3.2 2.5.6 3.6.1.3 0 .7-.2 1z"/></svg>
        877-555-0143
      </li>
      <li>
        <svg viewBox="0 0 24 24"><rect x="6" y="2" width="12" height="20" rx="2" fill="#fff"/><rect x="8" y="5" width="8" height="11" fill="var(--brand-blue)"/><circle cx="12" cy="19" r="1.2" fill="var(--brand-blue)"/></svg>
        515-555-0178
      </li>
      <li>
        <svg viewBox="0 0 24 24"><circle cx="12" cy="12" r="4" fill="none" stroke="#fff" stroke-width="2.4"/><path d="M16 8v5.5a2.5 2.5 0 0 0 5 0V12a9 9 0 1 0-4 7.5" fill="none" stroke="#fff" stroke-width="2.4"/></svg>
        rfeatherstone@limbnestler-example.com
      </li>
      <li>
        <svg viewBox="0 0 24 24"><g fill="none" stroke="#fff" stroke-width="1.8"><circle cx="12" cy="12" r="9"/><ellipse cx="12" cy="12" rx="4" ry="9"/><path d="M3 12h18M5 7h14M5 17h14"/></g></svg>
        www.Limbnestler-example.com
      </li>
    </ul>

    <div class="brand-block">
      <div class="brand-name"><span class="brand-dot"></span>Limb Nestler</div>
      <div class="brand-tagline">naturally made in the US</div>
    </div>
  </div>
</body>
</html>
```